Need a business card for our overland brand!

We had the logo made and we need a great design for our business card. Use the logo provide or tweak it however you see fit.

Contact Information for Business Card

Name, Title, Telephone, email, website

```html
<!DOCTYPE html>
<html lang="en">
<head>
<meta charset="utf-8">
<title>Summit Trailways — Business Card</title>
<link href="https://fonts.googleapis.com/css2?family=Roboto+Condensed:wght@400;700&display=swap" rel="stylesheet">
<style>
  :root {
    --bg-light: #eef0f3;
    --bg-dark: #c9ced6;
    --navy: #1f3650;
    --navy-deep: #1a2e45;
    --navy-text: #24364d;
    --accent: #2596be;
    --paper: #f7f8f9;
    --map-tone: #dcdfe3;
    --rule: #2a3b52;
  }
  * { margin: 0; padding: 0; box-sizing: border-box; }
  html, body { width: 1200px; height: 675px; overflow: hidden; }
  body {
    background: radial-gradient(ellipse at 40% 60%, var(--bg-light), var(--bg-dark));
    font-family: "Roboto Condensed", sans-serif;
    position: relative;
  }
  .card {
    position: absolute;
    top: 195px;
    width: 500px;
    height: 286px;
    border-radius: 3px;
    box-shadow: 0 10px 30px rgba(30, 40, 60, 0.22);
    overflow: hidden;
  }
  .card--front { left: 60px; background: linear-gradient(135deg, var(--navy-deep), var(--navy)); }
  .card--back { left: 640px; background: var(--paper); }

  .brand-name {
    font-weight: 700;
    text-transform: uppercase;
    line-height: 0.92;
    letter-spacing: 0.5px;
  }
  .card--front .brand-name {
    position: absolute;
    left: 0; right: 0; top: 88px;
    text-align: center;
    font-size: 58px;
    color: #2a4866;
  }

  .world-map {
    position: absolute;
    left: 40px; top: 40px;
    width: 440px; height: 210px;
    background: radial-gradient(ellipse at 55% 50%, var(--map-tone), rgba(220,223,227,0) 72%);
  }
  .card--back .brand-name {
    position: absolute;
    left: 36px; top: 104px;
    width: 200px;
    font-size: 44px;
    color: var(--navy-text);
  }
  .divider {
    position: absolute;
    left: 250px; top: 82px;
    width: 1px; height: 120px;
    background: var(--rule);
  }
  .contact {
    position: absolute;
    left: 266px; top: 80px;
    color: var(--navy-text);
  }
  .contact__name { font-weight: 700; font-size: 21px; text-transform: uppercase; letter-spacing: 0.5px; }
  .contact__title { font-size: 15px; color: var(--accent); margin-bottom: 8px; }
  .contact__list { list-style: none; }
  .contact__item {
    display: flex; align-items: center; gap: 7px;
    font-size: 14px; line-height: 22px;
  }
  .contact__item svg { width: 12px; height: 12px; flex: none; fill: var(--accent); }
  .contact__item--phone { letter-spacing: 2px; }
</style>
</head>
<body>
  <section class="card card--front">
    <div class="brand-name">Summit<br>Trailways</div>
  </section>

  <section class="card card--back">
    <div class="world-map" role="img" aria-label="Dotted world map background"></div>
    <div class="brand-name">Summit<br>Trailways</div>
    <div class="divider"></div>
    <div class="contact">
      <div class="contact__name">Dana Keller</div>
      <div class="contact__title">Director</div>
      <ul class="contact__list">
        <li class="contact__item contact__item--phone">
          <svg viewBox="0 0 12 12" aria-hidden="true"><path d="M2.5 0.5l2 2.5-1.2 1.3c.6 1.5 1.8 2.7 3.3 3.3L7.9 6.4l2.6 2-1 2.6C5 11 1 7 .8 2.3z"/></svg>
          +852 5550 4127
        </li>
        <li class="contact__item">
          <svg viewBox="0 0 12 12" aria-hidden="true"><path d="M0 2h12v8H0z M0.6 2.6L6 6.6l5.4-4" fill="var(--accent)"/><path d="M0.8 2.8L6 6.6l5.2-3.8" fill="none" stroke="#fff" stroke-width="0.9"/></svg>
          info@summittrailways.com
        </li>
        <li class="contact__item">
          <svg viewBox="0 0 12 12" aria-hidden="true"><circle cx="6" cy="6" r="5.5"/><path d="M0.5 6h11M6 0.5v11M6 .5c-3 3-3 8 0 11M6 .5c3 3 3 8 0 11" stroke="#fff" stroke-width="0.7" fill="none"/></svg>
          www.summittrailways.com
        </li>
      </ul>
    </div>
  </section>
</body>
</html>
```